Bramblewick Homes Ostrava Customer Brochure

Need a brochure designed that is clean and minimal that contains our logo, and contact information. Would like an area where we could insert business cards, and slips on both sides of the openings to place sheets of paper in. Would prefer to have the COVER LETTER I have attached printed on one side of the opening.

Target Market(s)

Home buyers

Font styles to use
Sans Serif

Colors

Designer to choose colors to be used in the design.

Requirements
Must have
• Logo, contact info, website, etc. Must be minimal in design and very clean looking.
Nice to have
• Please see above
Should not have
• No stock pictures of homes, builds, etc. Need it to look very clean

```html
<!DOCTYPE html>
<html lang="en">
<head>
<meta charset="utf-8">
<title>Bramblewick Homes Ostrava – Brochure</title>
<link href="https://fonts.googleapis.com/css2?family=Lato:wght@400;700&display=swap" rel="stylesheet">
<style>
  :root{
    --stage:#555555;
    --tan:#d1a77a;
    --tan-deep:#b8895a;
    --ink:#2b2b2b;
    --heading:#b07a3e;
    --paper:#ffffff;
    --fold:#b4b4b4;
  }
  *{box-sizing:border-box;margin:0;padding:0}
  html,body{width:1200px;height:1200px;overflow:hidden;background:var(--stage);font-family:"Lato",sans-serif}
  .spread{position:absolute;left:269px;width:662px;height:472px;display:flex}
  .spread--covers{top:60px}
  .spread--inside{top:669px}
  .page{position:relative;width:331px;height:472px;overflow:hidden;background:var(--paper)}
  .page--left-shade{background:linear-gradient(90deg,#fff 0%,#fff 62%,#ececec 84%,var(--fold) 100%)}
  .page--inside-shade{background:linear-gradient(90deg,#fff 0%,#f6f6f6 50%,#e2e2e2 88%,#d6d6d6 100%)}
  .page svg.art{position:absolute;inset:0;width:100%;height:100%}
  .brand{position:absolute;left:0;right:0;display:flex;flex-direction:column;align-items:center;font-weight:700;text-transform:uppercase;line-height:1}
  .brand__mark{width:26px;height:26px;background:var(--ink);margin-bottom:4px}
  .brand__name{font-size:6px;letter-spacing:.3px;color:var(--ink)}
  .brand--cover{top:30px;flex-direction:row;justify-content:center;gap:6px}
  .brand--cover .brand__mark{width:22px;height:22px;background:var(--paper);margin:0}
  .brand--cover .brand__name{font-size:13px;color:var(--paper);letter-spacing:.5px;line-height:1.05}
  .brand--inside{top:28px}
  .contact-strip{position:absolute;left:45px;bottom:13px;font-size:5.4px;font-weight:700;color:#fff;letter-spacing:.1px}
  .contact-strip span{padding:0 3px}
  .cover-web{position:absolute;left:0;right:0;bottom:13px;text-align:center;font-size:8.6px;color:var(--ink)}
  .letter{position:absolute;left:44px;width:245px;top:107px;font-size:4.9px;line-height:1.45;color:var(--ink);text-align:justify}
  .letter p{margin-bottom:4.4px}
  .letter .sign{margin-top:10px}
  .profile-title{position:absolute;left:0;right:0;top:138px;text-align:center;font-size:6.4px;font-weight:700;color:var(--heading);letter-spacing:.2px}
  .profile{position:absolute;left:44px;width:245px;top:160px;font-size:4.9px;line-height:1.45;color:var(--ink);text-align:justify}
  .profile p{margin-bottom:5px}
  .footer-rule{position:absolute;left:44px;width:245px;top:383px;height:1.5px;background:var(--tan)}
  .footer-address{position:absolute;left:52px;top:387px;font-size:4.2px;color:var(--ink)}
  .footer-address--right{left:auto;right:52px}
  .card-slot{position:absolute;left:108px;top:407px;width:102px;height:50px;background:var(--paper);display:flex;align-items:center;justify-content:center;gap:4px;box-shadow:0 0 3px rgba(0,0,0,.15)}
  .card-slot .brand__mark{width:12px;height:12px;background:var(--tan);margin:0}
  .card-slot .brand__name{font-size:8px;color:var(--tan);font-weight:700;text-transform:uppercase;line-height:1.05}
</style>
</head>
<body>

<section class="spread spread--covers">
  <div class="page page--left-shade">
    <svg class="art" viewBox="0 0 414 590" preserveAspectRatio="none" aria-hidden="true">
      <defs><linearGradient id="bandL" x1="0" x2="1"><stop offset="0" stop-color="#d1a77a"/><stop offset=".7" stop-color="#c99e70"/><stop offset="1" stop-color="#a9835b"/></linearGradient></defs>
      <polyline points="0,558 208,520 414,553" fill="none" stroke="#d1a77a" stroke-width="1.6"/>
      <polygon points="0,565 208,528 414,562 414,590 0,590" fill="url(#bandL)"/>
    </svg>
    <div class="contact-strip">420-555-0148<span>|</span>info@bramblewickhomesostrava.com<span>|</span>www.bramblewickhomesostrava.com</div>
  </div>

  <div class="page" style="background:var(--tan)">
    <svg class="art" viewBox="0 0 414 590" preserveAspectRatio="none" aria-hidden="true">
      <polygon points="0,555 208,520 414,553 414,590 0,590" fill="#fff"/>
      <polygon points="0,563 208,528 414,561 414,555 208,520 0,556" fill="#d1a77a"/>
    </svg>
    <div class="brand brand--cover"><span class="brand__mark"></span><span class="brand__name">Bramblewick<br>Homes</span></div>
    <div class="cover-web">www.bramblewickhomesostrava.com</div>
  </div>
</section>

<section class="spread spread--inside">
  <div class="page page--inside-shade">
    <svg class="art" viewBox="0 0 414 590" preserveAspectRatio="none" aria-hidden="true">
      <polygon points="0,508 208,475 414,508 414,590 0,590" fill="#d1a77a"/>
      <polyline points="0,508 208,475 414,508" fill="none" stroke="#fff" stroke-width="6"/>
    </svg>
    <div class="footer-rule"></div>
    <div class="footer-address">27 LIPOVA ST</div>
    <div class="footer-address footer-address--right">FAX: 420-555-0162</div>
    <div class="brand brand--inside"><span class="brand__mark"></span><span class="brand__name">Bramblewick Homes</span></div>
    <div class="letter">
      <p>Dear Sir/Madam:</p>
      <p>Welcome to the new vision of home building in Ostrava. For too long, the building and development business has been saddled with a poor image. Cost overruns, missed deadlines, and poor workmanship has led to most consumers feeling uneasy on building a new home. Unfortunately, in most cases, this image is warranted.</p>
      <p>When we started The Bramblewick Group in 1992, we vowed do our utmost to dispel the industry of this negative rap. We wanted to make honesty, solid workmanship, and above all, excellent service our hallmarks.</p>
      <p>Quite often, the language used by builders to describe their homes can be difficult for consumers to understand. At Bramblewick Homes, we value the opportunity to sit down with each and every client to explain any confusing terminology, as well as absorb as much input as we can from you, the purchaser. Furthermore, this ensures that there are no misconceptions or misunderstandings that exist between us and our clients before executing any contract. We go to great lengths to maintain our hallmarks and to ensure that we have nothing but satisfied customers.</p>
      <p>There couldn't be a better time to build a new home in the Ostrava Region. Industries are booming, and the beautiful landscape this region has to offer has led to new citizens flocking down here in recent years. From the wineries and restaurants to the picturesque views and kind neighbors, the region of Ostrava has become a desirable spot for families of all types.</p>
      <p>The time is now to make your dreams a reality. We look forward to the opportunity to build your dream home in the near future, and if you have any questions, please do not hesitate to ask myself, or a member of my staff.</p>
      <p class="sign">Yours truly,</p>
      <p class="sign">Marek Holub<br>Founder and President</p>
    </div>
  </div>

  <div class="page">
    <svg class="art" viewBox="0 0 414 590" preserveAspectRatio="none" aria-hidden="true">
      <polygon points="0,508 208,475 414,508 414,590 0,590" fill="#d1a77a"/>
      <polyline points="0,508 208,475 414,508" fill="none" stroke="#fff" stroke-width="6"/>
    </svg>
    <div class="footer-rule"></div>
    <div class="footer-address">27 LIPOVA ST</div>
    <div class="footer-address footer-address--right">FAX: 420-555-0162</div>
    <div class="brand brand--inside"><span class="brand__mark"></span><span class="brand__name">Bramblewick Homes</span></div>
    <h2 class="profile-title">CORPORATE PROFILE</h2>
    <div class="profile">
      <p>At Bramblewick Homes (Ostrava), we believe that there is only way to build a new home; with pride in one's craft and superior workmanship. The fact is; however, quality construction can be hard to find. Our staff at Bramblewick Homes is committed to changing that. From starter homes to dreamy custom builds, we construct each as if it were our own.</p>
      <p>We use only superior materials and employ first rate and dedicated trades to ensure that each house is given the utmost priority when it comes to quality. We take such care because we want to be proud of each home we build...just as proud as you will be living in it.</p>
      <p>Beginning in 1992, and stretching over 2 family generations, the Bramblewick Group has left a quality product in nearly every corner of the Ostrava Region. From our early work in the city centre, to our recent masterpieces in the outer districts, the results speak from themselves. Over the next few years, our endeavors will lead us into nearby towns and villages across the region. It is in these places where we will be pushing to create a "new age" of home building in the region.</p>
      <p>Building luxury homes has been a passion that this family has maintained for decades. You're encouraged to visit our website www.bramblewickhomesostrava.com for more information regarding all of our current and future developments. It is here that you will find a wide range of elevations and floor plans that we're constantly updating to ensure that each prospective client can find something that meets their tastes and needs.</p>
    </div>
    <div class="card-slot"><span class="brand__mark"></span><span class="brand__name">Bramblewick<br>Homes</span></div>
  </div>
</section>

</body>
</html>
```